Pull Up Banners

Would like to have these pull up banner designs changed to a new modern theme. I have running a sales booth and want to re-design the banner designs. I have uploaded old banner design, I need phone number and website added onto bottom. Happy to consider images to attract people attention to increase sales and spark people interest walking past.

```html
<!DOCTYPE html>
<html lang="en">
<head>
<meta charset="utf-8">
<title>NorthDesk Pull Up Banners</title>
<link href="https://fonts.googleapis.com/css2?family=Montserrat:ital,wght@0,400;0,500;0,600;0,700;0,800;1,500;1,700&display=swap" rel="stylesheet">
<style>
  :root{
    --orange:#f26522;
    --orange-soft:#f7935f;
    --ink:#161616;
    --white:#ffffff;
    --page:#ebebeb;
    --grey:#8a8a8a;
  }
  html,body{margin:0;padding:0;overflow:hidden;}
  body{width:1200px;height:2402px;background:var(--page);position:relative;font-family:'Montserrat',Arial,sans-serif;}
  .banner{position:absolute;top:496px;width:540px;height:1350px;overflow:hidden;box-shadow:0 2px 6px rgba(0,0,0,.12);}
  .banner--front{left:40px;}
  .banner--back{left:620px;}
  .banner-inner{position:absolute;left:0;top:0;width:431px;height:1077px;transform:scale(1.2529);transform-origin:0 0;}
  .banner-art{position:absolute;left:0;top:0;}
  .line{position:absolute;left:0;right:0;text-align:center;white-space:nowrap;}
  .brand{position:absolute;left:26px;top:30px;display:flex;align-items:center;gap:12px;}
  .brand-mark{width:38px;height:38px;border-radius:50%;background:var(--orange);}
  .brand-name{font-size:30px;font-weight:600;color:var(--ink);letter-spacing:2px;line-height:1;}
  .brand-tagline{position:absolute;left:76px;top:66px;font-size:6.2px;font-weight:600;letter-spacing:1.4px;color:var(--ink);}
  .headline-accent{color:var(--orange);font-weight:700;font-size:18px;}
  .headline-accent--large{font-size:27px;letter-spacing:.5px;}
  .headline-sub{color:var(--ink);font-weight:500;font-size:15px;line-height:1.2;}
  .leading-orange{color:var(--orange);font-weight:500;font-size:19px;}
  .leading-white{color:var(--white);font-weight:500;font-size:20px;}
  .pill-text{color:var(--ink);font-size:17px;font-weight:400;}
  .pill-text b{font-weight:700;}
  .service-label{position:absolute;width:90px;text-align:center;color:var(--white);font-size:7.6px;font-weight:700;line-height:1.2;}
  .cta-text{color:var(--white);font-size:16.5px;font-weight:700;letter-spacing:.5px;}
  .cta-note{color:var(--white);font-size:10px;font-style:italic;font-weight:500;}
  .cta-note b{font-weight:700;}
  .site-caption{font-size:6.5px;font-weight:700;letter-spacing:.5px;}
  .site-caption--light{color:var(--white);}
  .contact-line{position:absolute;left:55px;font-size:6.8px;font-weight:500;color:var(--ink);}
  .phone-number{position:absolute;left:273px;top:1009px;font-size:17.5px;font-weight:500;color:var(--ink);}
  .reason-title{color:var(--white);font-size:13px;font-weight:500;}
  .reason-detail{color:var(--orange);font-size:9.4px;font-weight:500;line-height:1.45;}
  .view-label{position:absolute;top:1870px;font-size:22px;font-weight:700;color:var(--orange);letter-spacing:1px;}
</style>
</head>
<body>

<!-- FRONT BANNER -->
<section class="banner banner--front">
  <div class="banner-inner">
    <svg class="banner-art" width="431" height="1077" viewBox="0 0 431 1077" xmlns="http://www.w3.org/2000/svg">
      <defs>
        <linearGradient id="fHeader" x1="0" y1="0" x2="0" y2="1"><stop offset="0" stop-color="#ffffff"/><stop offset="1" stop-color="#c9c9c9"/></linearGradient>
        <linearGradient id="fFooter" x1="0" y1="0" x2="0" y2="1"><stop offset="0" stop-color="#ffffff"/><stop offset="1" stop-color="#d6d6d6"/></linearGradient>
        <linearGradient id="fPhoto" x1="0" y1="0" x2="1" y2="1"><stop offset="0" stop-color="#9aa3ad"/><stop offset=".45" stop-color="#e9ecef"/><stop offset=".7" stop-color="#3f6fb5"/><stop offset="1" stop-color="#f2f2f2"/></linearGradient>
        <linearGradient id="fPill" x1="0" y1="0" x2="0" y2="1"><stop offset="0" stop-color="#ffffff"/><stop offset="1" stop-color="#bdbdbd"/></linearGradient>
      </defs>
      <rect width="431" height="1077" fill="#fff"/>
      <rect x="0" y="0" width="215" height="6" fill="var(--ink)"/>
      <rect x="215" y="0" width="216" height="6" fill="var(--orange)"/>
      <path d="M0 6H431V86Q230 92 0 112Z" fill="url(#fHeader)"/>
      <path d="M0 112Q230 92 431 86V97Q230 104 0 121Z" fill="var(--ink)"/>
      <path d="M0 121Q230 104 431 97V120Q300 110 0 126Z" fill="var(--orange)"/>
      <rect x="178" y="226" width="76" height="2" fill="var(--ink)"/>
      <rect x="215" y="226" width="39" height="2" fill="var(--orange)"/>
      <rect x="0" y="900" width="431" height="177" fill="url(#fFooter)"/>
      <rect x="0" y="470" width="431" height="230" fill="var(--ink)"/>
      <path d="M0 465Q230 572 431 458V478Q230 595 0 480Z" fill="var(--orange)"/>
      <path d="M0 455Q230 560 431 450V458Q230 572 0 465Z" fill="#fff"/>
      <path role="img" aria-label="Photo of a young technician in blue overalls repairing computer hardware with a screwdriver" d="M0 236H431V450Q230 560 0 455Z" fill="url(#fPhoto)"/>
      <path d="M0 680H431V915Q215 962 0 925Z" fill="var(--orange)"/>
      <path d="M0 931Q215 968 431 921" fill="none" stroke="#fff" stroke-width="2"/>
      <rect x="84" y="656" width="262" height="48" rx="24" fill="url(#fPill)" stroke="#fff" stroke-width="2"/>
      <g stroke="#fff" stroke-width="1" opacity=".8">
        <line x1="117" y1="738" x2="117" y2="852"/><line x1="215" y1="738" x2="215" y2="852"/><line x1="313" y1="738" x2="313" y2="852"/>
      </g>
      <g fill="var(--orange-soft)"><circle cx="68" cy="776" r="38"/><circle cx="166" cy="776" r="38"/><circle cx="264" cy="776" r="38"/><circle cx="362" cy="776" r="38"/></g>
      <g fill="#fff"><circle cx="68" cy="776" r="31"/><circle cx="166" cy="776" r="31"/><circle cx="264" cy="776" r="31"/><circle cx="362" cy="776" r="31"/></g>
      <path d="M52 786a8 8 0 0 1 2-15a11 11 0 0 1 21-2a8 8 0 0 1 8 17Z" fill="none" stroke="var(--orange)" stroke-width="2.2"/>
      <g transform="translate(163 776)">
        <circle r="11" fill="none" stroke="var(--orange)" stroke-width="5" stroke-dasharray="4 3"/>
        <circle r="8" fill="var(--orange)"/><circle r="3.5" fill="#fff"/>
        <g stroke="var(--orange)" stroke-width="2"><line x1="15" y1="-8" x2="22" y2="-8"/><line x1="15" y1="0" x2="24" y2="0"/><line x1="15" y1="8" x2="22" y2="8"/></g>
      </g>
      <g transform="translate(264 776)" fill="none" stroke="var(--orange)" stroke-width="2">
        <rect x="-17" y="-13" width="26" height="18" rx="1.5"/><line x1="-4" y1="5" x2="-4" y2="11"/><line x1="-10" y1="11" x2="2" y2="11"/>
        <rect x="12" y="-13" width="7" height="24" rx="1"/>
      </g>
      <g transform="translate(362 776)">
        <circle cy="-6" r="7.5" fill="var(--orange)"/>
        <path d="M-15 16Q-14 3 0 3Q14 3 15 16Z" fill="var(--orange)"/>
        <path d="M-10 -5A10 10 0 0 1 10 -5" fill="none" stroke="var(--orange)" stroke-width="2"/>
        <rect x="-12" y="-7" width="4" height="7" rx="1.5" fill="var(--orange)"/><rect x="8" y="-7" width="4" height="7" rx="1.5" fill="var(--orange)"/>
      </g>
      <rect x="88" y="877" width="254" height="35" rx="17.5" fill="var(--ink)"/>
      <g stroke="#fff" stroke-width=".6" opacity=".7"><line x1="95" y1="948" x2="118" y2="948"/><line x1="313" y1="948" x2="336" y2="948"/></g>
      <circle cx="33" cy="1003" r="10" fill="var(--orange)"/>
      <g transform="translate(33 1003)" fill="none" stroke="#fff" stroke-width="1.1"><circle r="5.5"/><ellipse rx="2.5" ry="5.5"/><line x1="-5.5" x2="5.5"/></g>
      <circle cx="33" cy="1035" r="10" fill="var(--orange)"/>
      <g transform="translate(33 1035)" fill="none" stroke="#fff" stroke-width="1.1"><rect x="-5.5" y="-4" width="11" height="8"/><path d="M-5.5 -4L0 1L5.5 -4"/></g>
      <line x1="233" y1="991" x2="233" y2="1052" stroke="var(--ink)" stroke-width="1.2"/>
      <path d="M251 1012c1-3 4-3 5-1l2 4c1 2 0 3-1 4c1 3 3 5 6 6c1-1 2-2 4-1l4 2c2 1 2 4-1 5c-3 2-8 1-13-4s-7-11-6-15z" fill="var(--orange)"/>
      <path d="M262 1010a8 8 0 0 1 8 8M262 1005a13 13 0 0 1 13 13" fill="none" stroke="var(--orange)" stroke-width="1.4"/>
      <rect x="0" y="1072" width="215" height="5" fill="var(--ink)"/>
      <rect x="215" y="1072" width="216" height="5" fill="var(--orange)"/>
    </svg>

    <div class="brand"><span class="brand-mark"></span><span class="brand-name">NORTHDESK</span></div>
    <div class="brand-tagline">YOUR PARTNER FOR ALL I.T SOLUTIONS</div>

    <div class="line headline-accent" style="top:150px;">IT SUPPORT MELBOURNE</div>
    <div class="line headline-sub" style="top:176px;">TAKING CARE OF YOUR<br>IT HEADACHES</div>

    <div class="line leading-orange" style="top:571px;">MELBOURNE’S LEADING</div>
    <div class="line leading-white" style="top:603px;">IT SUPPORT</div>

    <div class="line pill-text" style="top:668px;">OUR <b>SOLUTIONS</b></div>

    <div class="service-label" style="left:23px;top:823px;">Business IT<br>Services</div>
    <div class="service-label" style="left:121px;top:823px;">Managed IT<br>Solutions</div>
    <div class="service-label" style="left:219px;top:823px;">Retail Service<br>Centre</div>
    <div class="service-label" style="left:317px;top:823px;">Cloud Suite and<br>Team Calling</div>

    <div class="line cta-text" style="top:884px;">TALK TO US TODAY</div>
    <div class="line cta-note" style="top:919px;">for <b>IT support</b> and <b>more!</b>...</div>
    <div class="line site-caption site-caption--light" style="top:944px;">WWW.NORTHDESKIT.COM.AU</div>

    <div class="contact-line" style="top:998px;">www.northdeskit.com.au</div>
    <div class="contact-line" style="top:1030px;">support@northdeskit.com.au</div>
    <div class="phone-number">1300 555 018</div>
  </div>
</section>

<!-- BACK BANNER -->
<section class="banner banner--back">
  <div class="banner-inner">
    <svg class="banner-art" width="431" height="1077" viewBox="0 0 431 1077" xmlns="http://www.w3.org/2000/svg">
      <defs>
        <linearGradient id="bHeader" x1="0" y1="0" x2="0" y2="1"><stop offset="0" stop-color="#ffffff"/><stop offset="1" stop-color="#c9c9c9"/></linearGradient>
        <linearGradient id="bFooter" x1="0" y1="0" x2="0" y2="1"><stop offset="0" stop-color="#ffffff"/><stop offset="1" stop-color="#d6d6d6"/></linearGradient>
        <linearGradient id="bPhoto" x1="0" y1="0" x2="1" y2="1"><stop offset="0" stop-color="#6d6f73"/><stop offset=".4" stop-color="#eceeef"/><stop offset=".7" stop-color="#3d6fb8"/><stop offset="1" stop-color="#f3efe9"/></linearGradient>
        <linearGradient id="bPill" x1="0" y1="0" x2="0" y2="1"><stop offset="0" stop-color="#ffffff"/><stop offset="1" stop-color="#bdbdbd"/></linearGradient>
      </defs>
      <rect width="431" height="1077" fill="#fff"/>
      <rect x="0" y="0" width="215" height="6" fill="var(--ink)"/>
      <rect x="215" y="0" width="216" height="6" fill="var(--orange)"/>
      <path d="M0 6H431V86Q230 92 0 112Z" fill="url(#bHeader)"/>
      <path d="M0 112Q230 92 431 86V97Q230 104 0 121Z" fill="var(--ink)"/>
      <path d="M0 121Q230 104 431 97V120Q300 110 0 126Z" fill="var(--orange)"/>
      <rect x="172" y="227" width="88" height="2" fill="var(--ink)"/>
      <rect x="215" y="227" width="45" height="2" fill="var(--orange)"/>
      <rect x="0" y="900" width="431" height="177" fill="url(#bFooter)"/>
      <path d="M0 470H431V940Q215 1010 0 948Z" fill="var(--ink)"/>
      <path d="M0 478Q230 545 431 438V460Q230 568 0 494Z" fill="var(--orange)"/>
      <path d="M0 470Q230 532 431 430V438Q230 545 0 478Z" fill="#fff"/>
      <path role="img" aria-label="Photo of a young technician in blue overalls fitting cables inside an open desktop computer tower" d="M0 215H431V430Q230 532 0 470Z" fill="url(#bPhoto)"/>
      <rect x="118" y="580" width="196" height="33" rx="16.5" fill="url(#bPill)" stroke="#fff" stroke-width="1.5"/>
      <g stroke="#555" stroke-width=".7">
        <line x1="95" y1="699" x2="336" y2="699"/><line x1="95" y1="751" x2="336" y2="751"/><line x1="95" y1="818" x2="336" y2="818"/><line x1="95" y1="863" x2="336" y2="863"/>
        <line x1="50" y1="937" x2="112" y2="937"/><line x1="319" y1="937" x2="381" y2="937"/>
      </g>
      <circle cx="33" cy="1003" r="10" fill="var(--orange)"/>
      <g transform="translate(33 1003)" fill="none" stroke="#fff" stroke-width="1.1"><circle r="5.5"/><ellipse rx="2.5" ry="5.5"/><line x1="-5.5" x2="5.5"/></g>
      <circle cx="33" cy="1035" r="10" fill="var(--orange)"/>
      <g transform="translate(33 1035)" fill="none" stroke="#fff" stroke-width="1.1"><rect x="-5.5" y="-4" width="11" height="8"/><path d="M-5.5 -4L0 1L5.5 -4"/></g>
      <line x1="233" y1="991" x2="233" y2="1052" stroke="var(--ink)" stroke-width="1.2"/>
      <path d="M251 1012c1-3 4-3 5-1l2 4c1 2 0 3-1 4c1 3 3 5 6 6c1-1 2-2 4-1l4 2c2 1 2 4-1 5c-3 2-8 1-13-4s-7-11-6-15z" fill="var(--orange)"/>
      <path d="M262 1010a8 8 0 0 1 8 8M262 1005a13 13 0 0 1 13 13" fill="none" stroke="var(--orange)" stroke-width="1.4"/>
      <rect x="0" y="1072" width="215" height="5" fill="var(--ink)"/>
      <rect x="215" y="1072" width="216" height="5" fill="var(--orange)"/>
    </svg>

    <div class="brand"><span class="brand-mark"></span><span class="brand-name">NORTHDESK</span></div>
    <div class="brand-tagline">YOUR PARTNER FOR ALL I.T SOLUTIONS</div>

    <div class="line headline-accent headline-accent--large" style="top:134px;">SPECIALISTS IN</div>
    <div class="line headline-sub" style="top:175px;font-size:16px;">MANAGED IT SERVICES AND<br>HELP DESK</div>

    <div class="line leading-orange" style="top:557px;font-weight:700;">WHY SHOULD YOU</div>
    <div class="line pill-text" style="top:585px;font-weight:700;font-size:18px;">CHOOSE US?</div>

    <div class="line reason-title" style="top:642px;">FULL RANGE OF SERVICES</div>
    <div class="line reason-detail" style="top:659px;">IT, telecommunications, network and server support,<br>cybersecurity services and more</div>
    <div class="line reason-title" style="top:709px;">STABILITY</div>
    <div class="line reason-detail" style="top:727px;">One single hub for all tech solution and IT needs</div>
    <div class="line reason-title" style="top:761px;">BETTER BUSINESS EFFICIENCY</div>
    <div class="line reason-detail" style="top:778px;">No more headaches with our project management and IT<br>solutions</div>
    <div class="line reason-title" style="top:824px;">ACCOUNTABILITY</div>
    <div class="line reason-detail" style="top:842px;">Monthly report systems and infrastructure checks</div>
    <div class="line reason-title" style="top:869px;">AFFORDABLE</div>
    <div class="line reason-detail" style="top:887px;">Half the price of employing internal IT.</div>

    <div class="line site-caption site-caption--light" style="top:933px;">WWW.NORTHDESKIT.COM.AU</div>

    <div class="contact-line" style="top:998px;">www.northdeskit.com.au</div>
    <div class="contact-line" style="top:1030px;">support@northdeskit.com.au</div>
    <div class="phone-number">1300 555 018</div>
  </div>
</section>

<div class="view-label" style="left:40px;">FRONT</div>
<div class="view-label" style="left:620px;">BACK</div>

</body>
</html>
```